3-4 Page Research Report Template

We want a template in MS Word that we can use to write up research reports. We want a similar feal as our newsletter and website - but we also want it to look more modern, yet stay in the financial service / investment research world.

Examples: http://media.brelvox.example/Documents/Asset_Allocation_Focus_March2013.pdf

http://www.taskirel.example/Home/Documents/Default.aspx?fileId=58082

Our website: www.hurmontadvisors.example
Our Newsletter: http://www.hurmontadvisors.example/DawlinBrief/2012/2012-11-12.pdf

We want 3 template pages - a cover or 1st page, a middle page and and last or end page.

Reason: I would like more than two designers to compare ideas. I was hoping for 5. This is designers not designs.

We are not looking for a new version of our Newsletter "The Dawlin Brief" - We want a template to publish other research articles. We shared The Dawlin Brief file to give you a better idea on what we currently like / use - though dated as it was designed in 2004. 

That doesn't mean we wont pick a template using The Dawlin Brief as example content. I just wanted to be clear. 

Target Market(s)

Sophisticated investors with over $1M in the market and investment professionals (financial advisors)

Industry/Entity Type

Investment

Requirements
Must have
• Space for disclosures at the end.
Ability to drop in tables and charts/graphs
Should not have
• Do not use the HMRA website masthead directly. Please be creative in helping is get a more modern and fresh design. I provided it as reference on what we already like (or did in 2004 when it was designed).

```html
<!DOCTYPE html>
<html lang="en">
<head>
<meta charset="utf-8">
<title>Research Report Cover</title>
<link rel="stylesheet" href="https://fonts.googleapis.com/css2?family=Source+Sans+3:wght@400;700&display=swap">
<style>
  :root {
    --brand-blue: #0a5299;
    --heading-blue: #0d4f94;
    --band-grey: #8c8782;
    --text-grey: #847e78;
    --photo-grey: #a6a6a6;
    --paper: #ffffff;
  }
  html, body {
    margin: 0;
    padding: 0;
    overflow: hidden;
    background: var(--paper);
  }
  .page {
    position: relative;
    width: 848px;
    height: 1200px;
    overflow: hidden;
    background: var(--paper);
    font-family: "Source Sans 3", "Myriad Pro", Arial, sans-serif;
  }
  .masthead-band {
    position: absolute;
    left: 41px;
    top: 54px;
    width: 767px;
    height: 77px;
    background: linear-gradient(90deg, #8a8580, #908b86 50%, #8a8580);
  }
  .author-photo {
    position: absolute;
    left: 41px;
    top: 144px;
    width: 183px;
    height: 215px;
    background: linear-gradient(180deg, #b3b3b3 0%, #9c9c9c 60%, #3a3a3c 100%);
  }
  .brand {
    position: absolute;
    left: 600px;
    top: 160px;
    width: 208px;
    height: 140px;
  }
  .brand-mark {
    position: absolute;
    left: 36px;
    top: 0;
    width: 136px;
    height: 136px;
    border-radius: 50%;
    background: #d6d4d1;
  }
  .brand-name {
    position: absolute;
    left: 0;
    top: 52px;
    width: 208px;
    text-align: center;
    font-size: 24px;
    line-height: 28px;
    font-weight: 400;
    color: var(--brand-blue);
  }
  .report-title {
    position: absolute;
    left: 47px;
    top: 402px;
    margin: 0;
    font-size: 32px;
    line-height: 40px;
    font-weight: 700;
    color: var(--heading-blue);
  }
  .report-summary {
    position: absolute;
    left: 47px;
    top: 465px;
    width: 760px;
    margin: 0;
    font-size: 18.4px;
    line-height: 24px;
    font-weight: 700;
    color: var(--text-grey);
  }
  .cover-chart {
    position: absolute;
    left: 0;
    top: 0;
  }
  .cover-chart rect {
    fill: var(--brand-blue);
  }
</style>
</head>
<body>
<div class="page">
  <div class="masthead-band" role="img" aria-label="Grey band with flowing line pattern"></div>

  <div class="author-photo" role="img" aria-label="Portrait photograph of the report author"></div>

  <div class="brand">
    <div class="brand-mark"></div>
    <div class="brand-name">Hurmont Advisors</div>
  </div>

  <h1 class="report-title">Lorem ipsum dolor sit amet</h1>
  <p class="report-summary">Morbi euismod sem eget neque consectetur a ultrices nunc porta. Pellentesque pharetra, lacus pharetra vehicula consequat, neque est luctus mauris, at lobortis mauris elit ac felis. Vestibulum blandit nulla at massa lacinia suscipit.</p>

  <svg class="cover-chart" width="848" height="1200" viewBox="0 0 848 1200" aria-hidden="true">
    <rect x="41" y="591" width="81" height="574"/>
    <rect x="139" y="704" width="82" height="461"/>
    <rect x="237" y="838" width="82" height="327"/>
    <rect x="335" y="734" width="82" height="431"/>
    <rect x="433" y="815" width="82" height="350"/>
    <rect x="531" y="758" width="82" height="407"/>
    <rect x="629" y="704" width="82" height="461"/>
    <rect x="727" y="567" width="82" height="598"/>
  </svg>
</div>
</body>
</html>
```